Wordpress Theme for Tidy Meadow

Template Needs the Following:
-Main Index / home page
-Single post
-Single page
-Archives / All Articles
-Category Archives template
-Sub-Category Archives template
-Header
-Footer
Of course, must be responsive and work on all devices.
Notes on Overall Design
-Color scheme not decided, but prefer a trustworthy blue, maybe a true blue for links and accent color. Mostly black and white.
-Very similar to corvanleth.com in look, style, feel, simplicity, but will have greater focus on images in articles.
-Site is dedicated to long-form, high quality, actionable, evergreen content. This is not a news site, but it will cover a broad variety of topics. Focus on value added over timeliness / 'newness'
-Design ideas are attached as images.
Notes on Single Post Page, Header, and Footer
-For header, Title (Tidy Meadow) should be left aligned, far left
-Title can be EITHER image or text. This is a must. Clicking title name / logo should go to tidymeadow.com
-For header, 'Articles', 'About', and 'Premium' can either be center or left aligned with the border of where actual articles can go
-Footer alignment shoot match header alignment (no title needed, though)
-Title should be left aligned
-Category should be link clickable and go to category archives
Home Page / About Page / Single Page
-url is just tidymeadow.com, NOT tidymeadow.com/about
-Same layout as single page layout
-Will be text based, center aligned, very simple
-Includes site header and footer
-Title should be center aligned
-No category or author tags
Main Archives
-3 Featured articles at the top are hand selected by Tidy Meadow, NOT the 3 newest articles
-Each Main Category is shown, with a hyperlink to that category's archive page. -Clicking 'More' brings you to this archive as well
-The 3 articles for each main category are text based (no images, to save space), -They are hand selected by Tidy Meadow staff, not the most recent articles in the category
-After the category headers, all articles on the entire site are listed by date
Category Archives & Sub-Category Archives
-Same layout as main archives, but with sub-categories where the archives page had categories.
-All articles in that category listed at end of page by date
-Sub-category archives has same layout as main archive and category archive, but with nothing just our 3 favorite articles and all sub category articles by date

```html
<!DOCTYPE html>
<html lang="en">
<head>
<meta charset="utf-8">
<title>Tidy Meadow</title>
<link href="https://fonts.googleapis.com/css2?family=Lato:wght@400;700&family=Lora:wght@400&display=swap" rel="stylesheet">
<style>
  :root {
    --ink: #111111;
    --body-ink: #1e1e1e;
    --paper: #ffffff;
    --rule: #e2e2e4;
    --panel: #eeeef0;
    --panel-border: #cfcfd2;
    --field-border: #b9b9bc;
    --accent: #0a8fc9;
    --footer-bg: #efeff1;
  }
  * { box-sizing: border-box; margin: 0; padding: 0; }
  html, body { width: 827px; height: 1200px; overflow: hidden; background: var(--paper); }
  body { position: relative; font-family: "Lora", Georgia, serif; color: var(--body-ink); }

  .site-header { position: absolute; left: 0; top: 0; width: 827px; height: 47px; border-bottom: 1px solid var(--rule); }
  .site-title { position: absolute; left: 21px; top: 13px; font-family: "Lato", Arial, sans-serif; font-weight: 700; font-size: 15px; color: var(--ink); text-decoration: none; letter-spacing: 0.1px; }
  .main-nav a { position: absolute; top: 20px; font-family: "Lato", Arial, sans-serif; font-weight: 700; font-size: 7.5px; color: var(--ink); text-decoration: none; letter-spacing: 0.2px; }

  .section-title { position: absolute; left: 233px; width: 362px; text-align: center; font-family: "Lato", Arial, sans-serif; font-weight: 700; font-size: 14.5px; color: var(--ink); line-height: 18px; }
  .copy { position: absolute; left: 233px; width: 362px; font-size: 8.9px; line-height: 14.4px; text-align: justify; color: var(--body-ink); }

  .signup { position: absolute; left: 233px; top: 860px; width: 368px; height: 205px; background: var(--panel); border: 1px solid var(--panel-border); }
  .signup-label { position: absolute; left: 0; top: 34px; width: 100%; text-align: center; font-family: "Lato", Arial, sans-serif; font-weight: 700; font-size: 9.5px; color: var(--ink); }
  .email-field { position: absolute; left: 68px; top: 72px; width: 226px; height: 30px; background: var(--paper); border: 1px solid var(--field-border); display: flex; align-items: center; padding-left: 13px; font-size: 8px; color: var(--body-ink); }
  .email-field svg { margin-right: 7px; }
  .signup-button { position: absolute; left: 106px; top: 125px; width: 147px; height: 33px; background: var(--accent); color: #ffffff; border: none; font-family: "Lato", Arial, sans-serif; font-weight: 700; font-size: 10px; letter-spacing: 0.3px; }

  .site-footer { position: absolute; left: 0; top: 1120px; width: 827px; height: 80px; background: var(--footer-bg); }
  .footer-links { position: absolute; left: 0; top: 38px; width: 100%; text-align: center; font-family: "Lato", Arial, sans-serif; font-size: 7.8px; color: var(--ink); }
  .footer-links a { color: var(--ink); text-decoration: none; }
  .footer-links .sep { margin: 0 5px; }
</style>
</head>
<body>
  <header class="site-header">
    <a class="site-title" href="https://tidymeadow.com">TIDY MEADOW</a>
    <nav class="main-nav">
      <a href="#" style="left:328px">ARTICLES</a>
      <a href="#" style="left:397px">ABOUT</a>
      <a href="#" style="left:462px">PREMIUM</a>
    </nav>
  </header>

  <main>
    <h1 class="section-title" style="top:86px">WELCOME TO TIDY MEADOW</h1>
    <p class="copy" style="top:131px">There are many variations of passages of Lorem Ipsum available, but the majority have suffered alteration in some form, by injected humour, or randomised words which don't look even slightly believable. If you are going to use a passage of Lorem Ipsum, you need to be sure there isn't anything embarrassing hidden in the middle of text. All the Lorem Ipsum generators on the Internet tend to repeat predefined.</p>
    <p class="copy" style="top:225px">It is a long established fact that a reader will be distracted by the readable content of a page when looking at its layout. The point of using Lorem Ipsum is that it has a more-or-less normal distribution of letters, as opposed to using 'Content here, content here', making it look like readable.</p>

    <h2 class="section-title" style="top:336px">THE MISSION</h2>
    <p class="copy" style="top:384px">There are many variations of passages of Lorem Ipsum available, but the majority have suffered alteration in some form, by injected humour.</p>
    <p class="copy" style="top:434px">It is a long established fact that a reader will be distracted by the readable content of a page when looking at its layout. The point of using Lorem Ipsum is that it has a more-or-less normal distribution of letters, as opposed to using 'Content here, content here', making it look like readable.</p>
    <p class="copy" style="top:509px">There are many variations of passages of Lorem Ipsum available, but the majority have suffered alteration in some form, by injected humour, or randomised words which don't look even slightly believable. If you are going to use a passage of Lorem Ipsum, you need to be sure there isn't anything embarrassing hidden in the middle of text. All the Lorem Ipsum generators on the Internet tend to repeat predefined.</p>
    <p class="copy" style="top:603px">The point of using Lorem Ipsum is that it has a more-or-less normal distribution of letters, as opposed to using 'Content here, content here', making it look like readable.</p>

    <h2 class="section-title" style="top:685px">JOIN US NOW</h2>
    <p class="copy" style="top:725px">It is a long established fact that a reader will be distracted by the readable content of a page when looking at its layout. The point of using Lorem Ipsum is that it has a more-or-less normal distribution of letters, as opposed to using 'Content here, content here', making it look like readable.</p>
    <p class="copy" style="top:803px">The point of using Lorem Ipsum is that it has a more-or-less normal distribution of letters, as opposed to using 'Content here, content here', making it look like readable.</p>

    <form class="signup">
      <p class="signup-label">MY EMAIL ADDRESS IS</p>
      <div class="email-field">
        <svg width="9" height="7" viewBox="0 0 9 7" aria-hidden="true">
          <rect x="0.5" y="0.5" width="8" height="6" fill="none" stroke="#333" stroke-width="0.9"/>
          <path d="M0.8 1 L4.5 4 L8.2 1" fill="none" stroke="#333" stroke-width="0.9"/>
        </svg>
        <span>E mail id</span>
      </div>
      <button class="signup-button" type="button">GET UPDATES</button>
    </form>
  </main>

  <footer class="site-footer">
    <p class="footer-links"><a href="#">Contact</a><span class="sep">|</span><a href="#">Disclaimer</a><span class="sep">|</span>Copyrights @ 2017 All Rights Reserved</p>
  </footer>
</body>
</html>
```